Wordpress Design Project (Darvy)

We need a wordpress design for an established auction and real estate company based in Pennsylvania. The winning design will incorporate a professional layout with and company logo in a very simple and clean layout.

Industry/Entity Type

Real Estate

Requirements
Must have
• Navigation:
1) Home; 2) Auctions; 3) Appraisals; 4) Real Estate; 5) FAQ; 6) About Us; 7) Contact Us.

Site will have overall layout of https://www.plumvesta.com/featured/regions/the-northeast. Home page will have logo and navigation at top. The navigation bar will also have social media icons (facebook, Google+, RSS, twitter) inside it. There will be text in the content area - use lorem ipsum. The image attached will be used below text (auctions.jpg) . Footer will have smaller company loogo, the attached affiliation logos and social media icons.

Logo attached. Color scheme will be black, gray, and red as accent color.
Nice to have
• navigation will have dropdowns, nice to have one represented - under auctions 'All Auctions' will be dropdown.

```html
<!DOCTYPE html>
<html lang="en">
<head>
<meta charset="utf-8">
<title>Darvy Auctioneers &amp; Appraisers</title>
<link rel="stylesheet" href="https://fonts.googleapis.com/css2?family=Cinzel:wght@400;700&family=Lora:wght@400&family=Ubuntu:wght@400;500&display=swap">
<style>
:root{
  --red:#d53c39;
  --red-dark:#b82f2d;
  --ink:#1e1e1e;
  --text:#222;
  --muted:#555;
  --page:#ececec;
  --header-top:#ffffff;
  --header-bottom:#e4e4e4;
  --frame:#8d8d8d;
  --footer:#1c1c1c;
  --footer-text:#d6d6d6;
  --dropdown:#2f2f2f;
}
*{box-sizing:border-box;margin:0;padding:0}
html,body{width:1165px;height:1200px;overflow:hidden}
body{position:relative;background:var(--page);font-family:Arial,Helvetica,sans-serif;color:var(--text)}
.site-header{position:absolute;left:0;top:0;width:1165px;height:106px;background:linear-gradient(var(--header-top),var(--header-bottom));border-bottom:1px solid #d0d0d0}
.brand{position:absolute;left:101px;top:20px;display:flex;align-items:center;gap:10px}
.brand-mark{width:64px;height:64px;background:var(--red);border-radius:3px}
.brand-name{font-family:'Cinzel',serif;font-weight:700;font-size:42px;color:var(--ink);line-height:1}
.social{position:absolute;left:894px;top:13px;display:flex;gap:7px}
.social span{width:31px;height:31px;border-radius:50%}
.social .s1{background:#3a8fd0}.social .s2{background:#34539a}.social .s3{background:#d84a33}.social .s4{background:#f08a1c}
.main-nav{position:absolute;top:74px;left:0;height:24px}
.main-nav a{position:absolute;top:0;font-size:13px;color:var(--text);text-decoration:none;white-space:nowrap;line-height:24px}
.main-nav a.active{color:var(--red)}
.main-nav i{position:absolute;top:2px;width:1px;height:24px;background:#c8c8c8}
.dropdown{position:absolute;left:467px;top:105px;width:120px;background:var(--dropdown);padding:4px 0}
.dropdown::before{content:"";position:absolute;left:21px;top:-7px;border:7px solid transparent;border-top:0;border-bottom-color:var(--dropdown)}
.dropdown a{display:block;color:#fff;font-size:12px;text-decoration:none;padding:0 9px;line-height:25px}
.dropdown a+a{border-top:1px solid #454545}
.hero{position:absolute;left:99px;top:135px;width:968px;height:312px;border:3px solid var(--frame);background:radial-gradient(circle at 85% 10%,#dd4a46,var(--red) 45%,var(--red-dark));color:#fff;text-align:center}
.hero-kicker{font-family:'Cinzel',serif;font-size:22px;letter-spacing:1px;margin-top:36px}
.hero-rule{width:890px;height:1px;background:rgba(255,255,255,.3);margin:12px auto 0}
.hero-title{font-family:'Cinzel',serif;font-weight:400;font-size:30px;color:#111;margin-top:10px;letter-spacing:.5px}
.hero-copy{font-family:'Ubuntu',sans-serif;font-size:13.5px;line-height:21.5px;width:910px;margin:22px auto 0;letter-spacing:.2px}
.listing{position:absolute;width:456px}
.photo{width:456px;height:212px;background:#fff;padding:4px;box-shadow:0 0 3px rgba(0,0,0,.35)}
.photo div{width:100%;height:100%}
.listing h3{font-family:'Lora',serif;font-weight:400;font-size:22px;color:var(--red);margin-top:10px;letter-spacing:.5px}
.listing p{font-size:14px;letter-spacing:.6px;margin-top:3px}
.location{position:absolute;right:0;top:229px;display:flex;align-items:center;gap:8px;font-size:14px;letter-spacing:.4px}
.site-footer{position:absolute;left:0;top:1093px;width:1165px;height:107px;background:var(--footer);border-top:4px solid #2c2c2c}
.footer-mark{position:absolute;left:103px;top:23px;width:55px;height:55px;background:linear-gradient(#9a9a9a,#5c5c5c);border-radius:3px}
.footer-nav{position:absolute;left:169px;top:34px;font-size:13.5px;color:var(--footer-text)}
.footer-nav span{margin:0 8px;color:#bbb}
.copyright{position:absolute;left:169px;top:62px;font-size:13.5px;color:var(--footer-text)}
.affiliations{position:absolute;left:876px;top:16px;width:190px;height:80px}
.affiliations span{position:absolute;background:#6a6a6a}
</style>
</head>
<body>
<header class="site-header">
  <div class="brand"><div class="brand-mark"></div><div class="brand-name">Darvy</div></div>
  <div class="social"><span class="s1"></span><span class="s2"></span><span class="s3"></span><span class="s4"></span></div>
  <nav class="main-nav">
    <a style="left:405px">Home</a><i style="left:460px"></i>
    <a class="active" style="left:485px">Auctions</a><i style="left:557px"></i>
    <a style="left:581px">Appraisals</a><i style="left:666px"></i>
    <a style="left:689px">Real Estate</a><i style="left:780px"></i>
    <a style="left:804px">FAQ</a><i style="left:851px"></i>
    <a style="left:875px">About Us</a><i style="left:952px"></i>
    <a style="left:976px">Contact Us</a>
  </nav>
</header>
<div class="dropdown"><a>Dimmy auctions</a><a>Simply is autions</a></div>

<section class="hero">
  <div class="hero-kicker">WHEN LOOKING AT ITS LAYOUT</div>
  <div class="hero-rule"></div>
  <h1 class="hero-title">MANY DESKTOP PUBLISHING PACKAGES WEB PAGE EDITORS</h1>
  <p class="hero-copy">Lorem Ipsum is simply dummy text of the printing and typesetting industry. Lorem Ipsum has been the industry's standard dummy text ever since the 1500s, when an unknown printer took a galley of type and scrambled it to make a type specimen book. It has survived not only five centuries, but also the leap into electronic typesetting, remaining essentially unchanged. It was popularised in the 1960s with the release of Letraset sheets containing Lorem Ipsum passages, and more recently with desktop publishing software like Aldus PageMaker including versions of Lorem Ipsum</p>
</section>

<article class="listing" style="left:101px;top:481px">
  <div class="photo"><div role="img" aria-label="Wooden doors and cabinets lined up in a warehouse" style="background:linear-gradient(90deg,#8a5a32,#5a2318 45%,#6e3a22 70%,#a08a6a)"></div></div>
  <h3>Doors &amp; Windows</h3><p>Lorem Ipsum has been the industry's</p>
  <div class="location"><svg width="22" height="30" viewBox="0 0 22 30"><path d="M11 1C5 1 1 5.5 1 11c0 7 10 18 10 18s10-11 10-18C21 5.5 17 1 11 1z" fill="#e8413a"/><circle cx="11" cy="11" r="4" fill="#222"/></svg>Washington, DC</div>
</article>

<article class="listing" style="left:606px;top:481px">
  <div class="photo"><div role="img" aria-label="Bathroom vanities with granite tops" style="background:linear-gradient(#c9b49a,#2c2a28 35%,#a8582a 55%,#8a4520)"></div></div>
  <h3>Table Simply Dimmy</h3><p>Lorem Ipsum has been the industry's</p>
  <div class="location"><svg width="22" height="30" viewBox="0 0 22 30"><path d="M11 1C5 1 1 5.5 1 11c0 7 10 18 10 18s10-11 10-18C21 5.5 17 1 11 1z" fill="#e8413a"/><circle cx="11" cy="11" r="4" fill="#222"/></svg>Washington, DC</div>
</article>

<article class="listing" style="left:101px;top:785px">
  <div class="photo"><div role="img" aria-label="Rolls of carpet stacked with price tags" style="background:linear-gradient(135deg,#6e6a62,#a8a08e 45%,#55524c)"></div></div>
  <h3>Home Carpet</h3><p>Lorem Ipsum has been the industry's</p>
  <div class="location"><svg width="22" height="30" viewBox="0 0 22 30"><path d="M11 1C5 1 1 5.5 1 11c0 7 10 18 10 18s10-11 10-18C21 5.5 17 1 11 1z" fill="#e8413a"/><circle cx="11" cy="11" r="4" fill="#222"/></svg>Washington, DC</div>
</article>

<article class="listing" style="left:606px;top:785px">
  <div class="photo"><div role="img" aria-label="Row of white and wooden doors with glass panes" style="background:linear-gradient(90deg,#b08840,#e6ecef 25%,#c9d0d6 60%,#9a6a40)"></div></div>
  <h3>Doors &amp; Windows</h3><p>Lorem Ipsum has been the industry's</p>
  <div class="location"><svg width="22" height="30" viewBox="0 0 22 30"><path d="M11 1C5 1 1 5.5 1 11c0 7 10 18 10 18s10-11 10-18C21 5.5 17 1 11 1z" fill="#e8413a"/><circle cx="11" cy="11" r="4" fill="#222"/></svg>Washington, DC</div>
</article>

<footer class="site-footer">
  <div class="footer-mark"></div>
  <div class="footer-nav">Home<span>|</span>Auctions<span>|</span>Appraisals<span>|</span>Real Estate<span>|</span>FAQ<span>|</span>About Us<span>|</span>Contact Us</div>
  <div class="copyright">Copyright © Darvy Auctioneers &amp; Appraisers.</div>
  <div class="affiliations">
    <span style="left:5px;top:4px;width:32px;height:32px;border-radius:3px"></span>
    <span style="left:58px;top:0;width:52px;height:40px;border-radius:50%"></span>
    <span style="left:133px;top:0;width:40px;height:40px;border-radius:50%"></span>
    <span style="left:5px;top:48px;width:34px;height:30px;border-radius:3px"></span>
    <span style="left:66px;top:48px;width:34px;height:30px;border-radius:3px"></span>
    <span style="left:130px;top:46px;width:52px;height:32px;border-radius:50%"></span>
  </div>
</footer>
</body>
</html>
```